IT Product Event Invitations

We are requesting the design of two invitations for a series of technological events that will be held between the company Tidewell Core and its partner in the Dominican Republic, Velorbit.
Both events represent the launch of the Tidewell Core brand in the Dominican Republic.
The first event is an elegant dinner aimed at the banking sector of the Dominican Republic to showcase the "Ledgerline Banking Suite" software.
Event information:
- Descriptive text for the invitation: Velorbit y Tidewell Core le invitan a descubrir cómo reducir costos, aumentar la automatización y mejorar la satisfacción de los clientes a través de una solución única para enfrentar los desafíos de la banca.
- Date: 25 de Septiembre
- Time: 7PM
- Location: El Mirtal, Av. Julio Benavente 318
In the invitation, consider using the colors of the Tidewell Core and Velorbit brands if possible. You can find the logos in the webpage
The second event is a wine tasting to present "Crestway Operations Hub" aimed at various industries.
Event information:
- Descriptive text for the invitation: Velorbit y Tidewell Core le invitan a conocer una solución que le permitirá a toda su empresa brindar una experiencia de servicio a otro nivel.
- Date: 26 de Septiembre
- Time: 7PM
In the invitation, consider using the colors of the Tidewell Core and Velorbit brands if possible. You can find the logos in the web page.
Both invitations must have a button for participant registration and that when you click on the image, it will direct you to a form.
Form for Ledgerline Banking Suite: https://signup.palvento-forms.example/event/k3rq9-banking-dinner-7xw2
Form for Crestway Operations Hub: https://signup.palvento-forms.example/event/m8vt4-wine-tasting-2jq5
Target Market(s)
Enterprise Customers
Industry/Entity Type
Technology
Look and feel
Each slider illustrates characteristics of the customer's brand and the style your logo design should communicate.

```html
<!DOCTYPE html>
<html lang="es">
<head>
<meta charset="utf-8">
<title>Invitaciones – Ledgerline Banking Suite y Crestway Operations Hub</title>
<link rel="stylesheet" href="https://fonts.googleapis.com/css2?family=Poppins:wght@400;500;800&display=swap">
<style>
  :root {
    --backdrop: #9b9b9b;
    --navy-deep: #10172f;
    --navy: #1a2750;
    --blue-glow: #1d5fa8;
    --cyan: #2aaae2;
    --white: #ffffff;
    --red: #c1272d;
    --ink: #05070d;
    --btn-top: #2a8fe0;
    --btn-bottom: #0d5cb8;
  }
  * { box-sizing: border-box; margin: 0; padding: 0; }
  html, body { width: 828px; height: 1200px; overflow: hidden; background: var(--backdrop); }
  .sheet { position: relative; width: 828px; height: 1200px; }
  .slot { position: absolute; top: 355px; width: 353px; height: 490px; overflow: hidden; }
  .slot-banking { left: 53px; }
  .slot-operations { left: 422px; }

  .invitation {
    position: absolute; top: 0; left: 0;
    width: 680px; height: 944px;
    transform: scale(0.5191); transform-origin: 0 0;
    overflow: hidden;
    font-family: "Poppins", sans-serif;
    color: var(--white);
    background:
      radial-gradient(ellipse 420px 340px at 95% 4%, rgba(42,170,226,.55), transparent 70%),
      radial-gradient(ellipse 500px 300px at 65% 78%, rgba(29,95,168,.55), transparent 70%),
      linear-gradient(160deg, var(--navy-deep) 0%, var(--navy) 55%, #132046 100%);
  }
  .tech-texture {
    position: absolute; inset: 0;
    background:
      radial-gradient(circle 120px at 85% 18%, rgba(127,211,245,.18), transparent 70%),
      radial-gradient(circle 150px at 15% 82%, rgba(42,170,226,.2), transparent 70%);
  }
  .frame { position: absolute; inset: 0; }
  .partners {
    position: absolute; top: 96px; left: 0; width: 100%;
    display: flex; justify-content: center; align-items: center; gap: 20px;
    font-size: 30px; font-weight: 500; line-height: 44px;
  }
  .partners .divider { width: 2px; height: 38px; background: var(--white); }
  .partners .dot { display: inline-block; width: 10px; height: 10px; border-radius: 50%; background: var(--cyan); margin-left: 6px; vertical-align: middle; }
  .title {
    position: absolute; top: 200px; left: 0; width: 100%;
    text-align: center; font-weight: 800; font-size: 72px; line-height: 66px;
    letter-spacing: -.5px; text-transform: uppercase;
  }
  .title .accent { color: var(--cyan); display: block; }
  .intro {
    position: absolute; top: 422px; left: 80px; width: 520px;
    text-align: center; font-size: 17px; line-height: 22px; font-weight: 400;
  }
  .slot-operations .intro { top: 434px; }
  .details {
    position: absolute; top: 546px; left: 83px; width: 514px; height: 74px;
    border-top: 2px solid var(--white); border-bottom: 2px solid var(--white);
    display: flex; align-items: center;
  }
  .details .date { width: 118px; font-size: 17px; line-height: 19px; text-align: center; }
  .details .sep { width: 2px; height: 52px; background: var(--cyan); }
  .details .time { width: 145px; text-align: center; color: var(--red); font-weight: 800; font-size: 56px; line-height: 1; }
  .details .place { display: flex; align-items: center; gap: 8px; padding-left: 14px; font-size: 17px; line-height: 19px; }
  .register {
    position: absolute; top: 660px; left: 152px; width: 376px; height: 78px;
    border-radius: 39px; padding: 5px;
    background: linear-gradient(180deg, #1b6fc4, #0a3f86);
    box-shadow: 0 5px 14px rgba(0,0,0,.45);
    text-decoration: none; display: block;
  }
  .register span {
    display: flex; width: 100%; height: 100%; border-radius: 34px;
    border: 2px solid var(--white);
    background: linear-gradient(180deg, var(--btn-top), var(--btn-bottom));
    align-items: center; justify-content: center;
    color: var(--white); font-weight: 800; font-size: 36px; letter-spacing: .3px;
  }
  .waves { position: absolute; left: 0; bottom: 0; }
</style>
</head>
<body>
<div class="sheet">

  <div class="slot slot-banking">
    <main class="invitation">
      <div class="tech-texture" role="img" aria-label="Fondo tecnológico con hexágonos y luces azules"></div>
      <svg class="frame" width="680" height="944" viewBox="0 0 680 944" aria-hidden="true">
        <polyline points="122,698 36,698 36,36 644,36 644,698 558,698" fill="none" stroke="#ffffff" stroke-width="4"/>
      </svg>
      <div class="partners">
        <span class="brand">Tidewell Core<i class="dot"></i></span>
        <span class="divider"></span>
        <span class="brand">Velorbit</span>
      </div>
      <h1 class="title">Ledgerline<br>Banking<span class="accent">Suite</span></h1>
      <p class="intro">Velorbit y Tidewell Core le invitan a descubrir cómo reducir costos, aumentar la automatización y mejorar la satisfacción de los clientes a través de una solución única para enfrentar los desafíos de la banca.</p>
      <div class="details">
        <div class="date">25 de<br>Septiembre</div>
        <div class="sep"></div>
        <div class="time">7PM</div>
        <div class="sep"></div>
        <div class="place">
          <svg width="18" height="25" viewBox="0 0 22 30" aria-hidden="true">
            <path d="M11 1C5.5 1 1 5.3 1 10.7 1 18 11 29 11 29s10-11 10-18.3C21 5.3 16.5 1 11 1z" fill="none" stroke="#ffffff" stroke-width="3"/>
            <circle cx="11" cy="11" r="3.5" fill="#ffffff"/>
          </svg>
          <span>El Mirtal, Av. Julio<br>Benavente 318</span>
        </div>
      </div>
      <a class="register" href="https://signup.palvento-forms.example/event/k3rq9-banking-dinner-7xw2"><span>REGISTER HERE</span></a>
      <svg class="waves" width="680" height="204" viewBox="0 740 680 204" aria-hidden="true">
        <defs>
          <linearGradient id="waveCyanA" x1="0" y1="0" x2="1" y2="0">
            <stop offset="0" stop-color="#2aaae2"/><stop offset=".6" stop-color="#2aaae2"/>
            <stop offset=".82" stop-color="#bfe9fb"/><stop offset="1" stop-color="#2aaae2"/>
          </linearGradient>
        </defs>
        <path d="M0,752 C120,820 210,900 345,880 C460,862 540,800 680,790 L680,944 L0,944 Z" fill="url(#waveCyanA)"/>
        <path d="M400,852 C500,802 590,782 680,784" fill="none" stroke="#05070d" stroke-width="6"/>
        <path d="M0,822 C140,902 250,922 360,902 C490,878 580,822 680,826 L680,950 L0,950 Z" fill="#1a2a5c" stroke="#05070d" stroke-width="6"/>
      </svg>
    </main>
  </div>

  <div class="slot slot-operations">
    <main class="invitation">
      <div class="tech-texture" role="img" aria-label="Fondo tecnológico con hexágonos y luces azules"></div>
      <svg class="frame" width="680" height="944" viewBox="0 0 680 944" aria-hidden="true">
        <polyline points="122,698 36,698 36,36 644,36 644,698 558,698" fill="none" stroke="#ffffff" stroke-width="4"/>
      </svg>
      <div class="partners">
        <span class="brand">Tidewell Core<i class="dot"></i></span>
        <span class="divider"></span>
        <span class="brand">Velorbit</span>
      </div>
      <h1 class="title">Crestway<br>Operations<span class="accent">Hub</span></h1>
      <p class="intro">Velorbit y Tidewell Core le invitan a conocer una solución que le permitirá a toda su empresa brindar una experiencia de servicio a otro nivel.</p>
      <div class="details">
        <div class="date">26 de<br>Septiembre</div>
        <div class="sep"></div>
        <div class="time">7PM</div>
        <div class="sep"></div>
        <div class="place">
          <svg width="18" height="25" viewBox="0 0 22 30" aria-hidden="true">
            <path d="M11 1C5.5 1 1 5.3 1 10.7 1 18 11 29 11 29s10-11 10-18.3C21 5.3 16.5 1 11 1z" fill="none" stroke="#ffffff" stroke-width="3"/>
            <circle cx="11" cy="11" r="3.5" fill="#ffffff"/>
          </svg>
          <span>El Mirtal, Av. Julio<br>Benavente 318</span>
        </div>
      </div>
      <a class="register" href="https://signup.palvento-forms.example/event/m8vt4-wine-tasting-2jq5"><span>REGISTER HERE</span></a>
      <svg class="waves" width="680" height="204" viewBox="0 740 680 204" aria-hidden="true">
        <defs>
          <linearGradient id="waveCyanB" x1="0" y1="0" x2="1" y2="0">
            <stop offset="0" stop-color="#2aaae2"/><stop offset=".6" stop-color="#2aaae2"/>
            <stop offset=".82" stop-color="#bfe9fb"/><stop offset="1" stop-color="#2aaae2"/>
          </linearGradient>
        </defs>
        <path d="M0,752 C120,820 210,900 345,880 C460,862 540,800 680,790 L680,944 L0,944 Z" fill="url(#waveCyanB)"/>
        <path d="M400,852 C500,802 590,782 680,784" fill="none" stroke="#05070d" stroke-width="6"/>
        <path d="M0,822 C140,902 250,922 360,902 C490,878 580,822 680,826 L680,950 L0,950 Z" fill="#1a2a5c" stroke="#05070d" stroke-width="6"/>
      </svg>
    </main>
  </div>

</div>
</body>
</html>
```